Modern Business Card

Modern professional business card with more than just logo and demographic info. Something memorable.

We are a trendy/modern chiropractic group with an emphasis on neurology, hence the minimalist-type brain logo. We want to convey that modern and technical aspect with professionalism and the elite nature of our practice environment.

```html
<!DOCTYPE html>
<html lang="en">
<head>
<meta charset="utf-8">
<title>Keystone Spine – Business Card</title>
<link rel="stylesheet" href="https://fonts.googleapis.com/css2?family=Open+Sans:wght@400;600;700&display=swap">
<style>
  :root {
    --brand-blue: #4680c2;
    --brand-blue-light: #9ab7de;
    --ink: #111111;
    --ink-soft: #555555;
    --paper: #ffffff;
    --canvas: #ffffff;
  }
  * { margin: 0; padding: 0; box-sizing: border-box; }
  html, body {
    width: 1200px; height: 1200px; overflow: hidden;
    background: var(--canvas);
    font-family: "Open Sans", Arial, sans-serif;
  }
  .sheet { position: relative; width: 1200px; height: 1200px; }
  .card {
    position: absolute; left: 115px; width: 969px; height: 554px;
    background: var(--paper);
    box-shadow: 0 0 8px rgba(0,0,0,0.12);
    overflow: hidden;
  }
  .card--front { top: 42px; }
  .card--back { top: 606px; }

  .band { position: absolute; left: 0; right: 0; height: 72px; }
  .band--top { top: 0; background: linear-gradient(180deg, var(--brand-blue) 0%, var(--brand-blue) 70%, var(--brand-blue-light) 100%); }
  .band--bottom { bottom: 0; background: linear-gradient(0deg, var(--brand-blue) 0%, var(--brand-blue) 70%, var(--brand-blue-light) 100%); }

  .wordmark {
    position: absolute; display: flex; align-items: center;
    color: var(--ink); font-weight: 600; letter-spacing: 0.02em; white-space: nowrap;
  }
  .wordmark__square { background: var(--brand-blue); flex: none; }
  .card--front .wordmark {
    left: 0; right: 0; top: 0; bottom: 0; justify-content: center; gap: 26px; font-size: 70px;
  }
  .card--front .wordmark__square { width: 80px; height: 80px; }
  .card--back .wordmark {
    left: 82px; top: 252px; gap: 14px; font-size: 38px;
  }
  .card--back .wordmark__square { width: 46px; height: 46px; }

  .contact { position: absolute; left: 534px; top: 112px; color: var(--ink-soft); }
  .contact__name { color: var(--ink); font-weight: 700; font-size: 33px; line-height: 42px; letter-spacing: 0.01em; }
  .contact__role { font-size: 26px; line-height: 34px; }
  .contact__address { margin-top: 48px; font-size: 25px; line-height: 36px; }
  .contact__list { list-style: none; margin-top: 20px; font-size: 26px; line-height: 37px; }
  .contact__item { display: flex; align-items: center; gap: 18px; }
  .contact__icon { width: 24px; height: 24px; fill: var(--brand-blue); flex: none; }
</style>
</head>
<body>
<div class="sheet">

  <section class="card card--front">
    <div class="band band--top" role="img" aria-label="Decorative blue wave band"></div>
    <div class="band band--bottom" role="img" aria-label="Decorative blue wave band"></div>
    <div class="wordmark"><span class="wordmark__square"></span>KEYSTONE SPINE</div>
  </section>

  <section class="card card--back">
    <div class="band band--top" role="img" aria-label="Decorative blue wave band"></div>
    <div class="band band--bottom" role="img" aria-label="Decorative blue wave band"></div>

    <div class="wordmark"><span class="wordmark__square"></span>KEYSTONE SPINE</div>

    <div class="contact">
      <p class="contact__name">DANIEL REYES</p>
      <p class="contact__role">President</p>
      <p class="contact__address">Street Name Here, Suite 100<br>Street Zip Code,Country</p>
      <ul class="contact__list">
        <li class="contact__item">
          <svg class="contact__icon" viewBox="0 0 24 24" aria-hidden="true"><path d="M6.6 10.8c1.4 2.8 3.8 5.1 6.6 6.6l2.2-2.2c.3-.3.7-.4 1-.2 1.1.4 2.3.6 3.6.6.6 0 1 .4 1 1V20c0 .6-.4 1-1 1C10.6 21 3 13.4 3 4c0-.6.4-1 1-1h3.5c.6 0 1 .4 1 1 0 1.3.2 2.5.6 3.6.1.3 0 .7-.2 1L6.6 10.8z"/></svg>
          <span>01234-56789</span>
        </li>
        <li class="contact__item">
          <svg class="contact__icon" viewBox="0 0 24 24" aria-hidden="true"><path d="M2 5h20v14H2V5zm2 2v.4l8 5.6 8-5.6V7H4zm16 2.8-8 5.6-8-5.6V17h16V9.8z"/></svg>
          <span>info@yourwebsite.com</span>
        </li>
        <li class="contact__item">
          <svg class="contact__icon" viewBox="0 0 24 24" aria-hidden="true"><path d="M12 2a10 10 0 1 0 0 20 10 10 0 0 0 0-20zm6.9 6h-3a15.7 15.7 0 0 0-1.3-3.6A8 8 0 0 1 18.9 8zM12 4c.8 1.2 1.5 2.5 1.9 4h-3.8c.4-1.5 1.1-2.8 1.9-4zM4.3 14a8 8 0 0 1 0-4h3.4a16 16 0 0 0 0 4H4.3zm.8 2h3c.3 1.3.8 2.5 1.3 3.6A8 8 0 0 1 5.1 16zm3-8h-3a8 8 0 0 1 4.3-3.6C8.9 5.5 8.4 6.7 8.1 8zM12 20c-.8-1.2-1.5-2.5-1.9-4h3.8c-.4 1.5-1.1 2.8-1.9 4zm2.3-6H9.7a14.7 14.7 0 0 1 0-4h4.6a14.7 14.7 0 0 1 0 4zm.3 5.6c.5-1.1 1-2.3 1.3-3.6h3a8 8 0 0 1-4.3 3.6zm1.7-5.6a16 16 0 0 0 0-4h3.4a8 8 0 0 1 0 4h-3.4z"/></svg>
          <span>www.yourwebsite.com</span>
        </li>
      </ul>
    </div>
  </section>

</div>
</body>
</html>
```